Need Label for Our Jams Product

HI,

we have are launching a new brand in the premium foods category by the name of Vo-Pantry. the logo has been designed and our first product is Premium 65% fruit Jams. we need a label for it now. can you help ?

our flavours are strawberry, apple, mango, blackberry, cherry, PineApple.

Please note that we need one design and then we will modify it according to the flavour. so you will need to make one flavour on a theme. and then we will apply the theme accordingly to the rest of the flavours.

Target Market(s)

Health concious people who donot want to use ordinary jams any further.

Industry/Entity Type

Product

Requirements
Must have
• the logo, not too big because we need the flavour name aswell on the front of the label.
also would appreciate a touch of fruit or similar
also please note that the colour of the cap in the attached picture is the actual colour. and the label should incline with the colour of cap aswell. im not saying the label to be in that colour, but must balance the whole look of the bottle.
Please note that this is a round bottle, so much information is needed on the front. the sides of the labels will be occupied by ingredients nutrition facts etc.
Nice to have
• white background but not necessary.
Should not have
• black colour

```html
<!DOCTYPE html>
<html lang="en">
<head>
<meta charset="utf-8">
<title>Vo-Pantry Premium Fruit Jam Label</title>
<link rel="stylesheet" href="https://fonts.googleapis.com/css2?family=Crimson+Text:wght@400;600&family=Lobster+Two:ital,wght@1,700&display=swap">
<style>
  :root {
    --paper: #ffffff;
    --guide: #3fe3f2;
    --dimension: #111111;
    --body-text: #5e4e36;
    --brand-green: #6cbf1e;
    --highlight: rgba(255, 255, 255, 0.85);
    --pineapple: #ffe100;
    --blackberry: #261b56;
    --mango: #f59a00;
    --cherry: #2b0914;
    --strawberry: #ff0a0a;
    --apple: #80ff00;
  }
  * { margin: 0; padding: 0; box-sizing: border-box; }
  html, body { width: 1200px; height: 900px; overflow: hidden; background: var(--paper); }
  .artboard { position: relative; width: 1200px; height: 900px; }

  .dimension { position: absolute; font: 12px/1 Arial, Helvetica, sans-serif; color: var(--dimension); }
  .dimension--width { left: 80px; top: 136px; width: 993px; height: 16px; }
  .dimension--height { left: 52px; top: 163px; width: 16px; height: 228px; }
  .dimension svg { position: absolute; inset: 0; overflow: visible; }
  .dimension__value { position: absolute; background: var(--paper); padding: 0 6px; }
  .dimension--width .dimension__value { left: 50%; top: 1px; transform: translateX(-50%); }
  .dimension--height .dimension__value { left: 50%; top: 50%; transform: translate(-50%, -50%) rotate(-90deg); white-space: nowrap; }

  .label { position: absolute; left: 90px; top: 173px; width: 1027px; height: 210px; border: 1.5px solid var(--guide); }
  .label__overlap { position: absolute; left: 971px; top: 0; bottom: 0; border-left: 1.5px solid var(--guide); }

  .copy-column {
    position: absolute; top: 30px; white-space: nowrap;
    font: 11.2px/13px "Crimson Text", Georgia, serif; color: var(--body-text);
  }
  .copy-column--1 { left: 19px; }
  .copy-column--2 { left: 192px; }
  .copy-column--3 { left: 612px; }
  .copy-column--4 { left: 780px; }

  .brand-name {
    position: absolute; left: 411px; top: 5px; width: 146px; text-align: center;
    font: 600 15px/1 "Crimson Text", Georgia, serif; color: var(--brand-green);
  }
  .label .fruit-tile { position: absolute; left: 411px; top: 31px; width: 146px; height: 146px; }
  .label .flavour-name { position: absolute; left: 411px; top: 177px; width: 146px; font-size: 19px; }

  .fruit-tile { display: block; background: radial-gradient(ellipse 38% 44% at 52% 55%, var(--highlight) 0%, var(--highlight) 55%, var(--tile) 100%); }
  .flavour-name {
    text-align: center; font-family: "Lobster Two", "Brush Script MT", cursive;
    font-style: italic; font-weight: 700; line-height: 1; color: var(--tile);
  }

  .flavour-range { position: absolute; left: 38px; top: 507px; display: flex; gap: 20px; }
  .flavour { width: 168px; }
  .flavour .fruit-tile { width: 168px; height: 168px; }
  .flavour .flavour-name { margin-top: 14px; font-size: 28px; }

  .flavour--pineapple { --tile: var(--pineapple); }
  .flavour--blackberry { --tile: var(--blackberry); }
  .flavour--mango { --tile: var(--mango); }
  .flavour--cherry { --tile: var(--cherry); }
  .flavour--strawberry { --tile: var(--strawberry); }
  .flavour--apple { --tile: var(--apple); }
</style>
</head>
<body>
<main class="artboard">

  <div class="dimension dimension--width">
    <svg width="993" height="16" viewBox="0 0 993 16">
      <line x1="2" y1="8" x2="991" y2="8" stroke="currentColor" stroke-width="1.2"/>
      <path d="M0 8 L12 3 L12 13 Z" fill="currentColor"/>
      <path d="M993 8 L981 3 L981 13 Z" fill="currentColor"/>
    </svg>
    <span class="dimension__value">224mm</span>
  </div>

  <div class="dimension dimension--height">
    <svg width="16" height="228" viewBox="0 0 16 228">
      <line x1="8" y1="2" x2="8" y2="226" stroke="currentColor" stroke-width="1.2"/>
      <path d="M8 0 L3 12 L13 12 Z" fill="currentColor"/>
      <path d="M8 228 L3 216 L13 216 Z" fill="currentColor"/>
    </svg>
    <span class="dimension__value">47.9mm</span>
  </div>

  <section class="label flavour--mango" aria-label="Mango jam wrap-around label">
    <p class="copy-column copy-column--1">Sed tempus, nibh in malesuada<br>posuere, enim tortor lacinia<br>tortor, vitae interdum mauris<br>diam sit amet est. Donec nec<br>nulla mauris. Maecenas velit<br>tellus, porttitor venenatis<br>consectetur et, varius id dolor.<br>Sed eget tortor eget nulla lobortis<br>dignissim sed et tellus. Vestibu-<br>lum aliquam, ipsum eu dictum<br>fringilla, tellus purus malesuada</p>
    <p class="copy-column copy-column--2">magna, quis ullamcorper enim<br>nulla non mi. Mauris tortor<br>augue, consequat neque. Donec<br>nec nulla mauris. Maecenas velit<br>tellus, porttitor venenatis<br>consectetur et, varius id dolor.<br>Sed eget tortor eget nulla lobortis<br>dignissim sed et tellus. Vestibu-<br>lum aliquam, ipsum eu dictum<br>fringilla, tellus purus ullamcorper<br>enim nulla non mi.</p>

    <div class="brand-name">Vo-Pantry</div>
    <div class="fruit-tile" role="img" aria-label="White mango silhouette with leaf on orange square"></div>
    <div class="flavour-name">Mango</div>

    <p class="copy-column copy-column--3">Premium 65% fruit Jams.<br>Lorem ipsum dolor sit amet,<br>consectetur adipiscing elit. Duis<br>rutrum dignissim ligula<br>malesuada lobortis. Integer eros<br>dui, sollicitudin vel adipiscing<br>vitae, semper in elit. Vivamus<br>rhoncus nulla libero, at lobortis<br>nibh. Mauris sit amet turpis in<br>ante cursus adipiscing. Sed dui<br>nulla, eleifend vel imperdiet eu,</p>
    <p class="copy-column copy-column--4">sollicitudin id quam. Duis<br>rutrum dignissim ligula<br>malesuada lobortis. Sed dui<br>nulla, eleifend vel. Duis rutrum<br>dignissim ligula malesuada<br>lobortis. Integer eros dui,<br>sollicitudin vel adipiscing vitae,<br>semper in elit. Vivamus rhoncus<br>nulla libero, at lobortis nibh.<br>Mauris sit amet turpis in ante<br>cursus adipiscing.</p>

    <div class="label__overlap"></div>
  </section>

  <section class="flavour-range" aria-label="Flavour variations">
    <figure class="flavour flavour--pineapple">
      <div class="fruit-tile" role="img" aria-label="White pineapple silhouette on yellow square"></div>
      <figcaption class="flavour-name">Pineapple</figcaption>
    </figure>
    <figure class="flavour flavour--blackberry">
      <div class="fruit-tile" role="img" aria-label="White blackberries and leaf silhouette on deep indigo square"></div>
      <figcaption class="flavour-name">Blackberry</figcaption>
    </figure>
    <figure class="flavour flavour--mango">
      <div class="fruit-tile" role="img" aria-label="White mango silhouette with leaf on orange square"></div>
      <figcaption class="flavour-name">Mango</figcaption>
    </figure>
    <figure class="flavour flavour--cherry">
      <div class="fruit-tile" role="img" aria-label="White cherry pair silhouette on dark burgundy square"></div>
      <figcaption class="flavour-name">Cherry</figcaption>
    </figure>
    <figure class="flavour flavour--strawberry">
      <div class="fruit-tile" role="img" aria-label="White strawberry silhouette on red square"></div>
      <figcaption class="flavour-name">Strawberry</figcaption>
    </figure>
    <figure class="flavour flavour--apple">
      <div class="fruit-tile" role="img" aria-label="White apple silhouette with leaf on lime green square"></div>
      <figcaption class="flavour-name">Apple</figcaption>
    </figure>
  </section>

</main>
</body>
</html>
```